Business Card Design for a Lending Business (Hard Money loans)

We need a business card for our Real Estate Lending business. We do hard Money loans for real estate investors. We have an existing logo we like, see attached. I'd like the business card to mostly include the logo colors, but a bright color pop of some sort would be nice to see also. Card should include Logo, Company Name, Company Address, Employee Name, Cell Phone, Main Phone, Email, Website

Industry/Entity Type

Finance / Lending

Contact Information for Business Card

Logo, Company Name, Company Address, Employee Name, Cell Phone, Main Phone, Email, Website

Requirements
Nice to have
• I'd like the business card to mostly include the logo colors, but a bright color pop of some sort would be nice to see also.

```html
<!DOCTYPE html>
<html lang="en">
<head>
<meta charset="utf-8">
<title>Harborline Lending – Business Card</title>
<link rel="stylesheet" href="https://fonts.googleapis.com/css2?family=Montserrat:wght@500;700&family=Roboto:wght@400&display=swap">
<style>
  :root {
    --backdrop: #999999;
    --card: #ffffff;
    --navy: #0a17a6;
    --aqua: #40e4f9;
    --white: #ffffff;
  }
  * { margin: 0; padding: 0; box-sizing: border-box; }
  html, body {
    width: 1196px;
    height: 1200px;
    overflow: hidden;
    background: var(--backdrop);
  }
  .canvas {
    position: relative;
    width: 1196px;
    height: 1200px;
  }
  .card {
    position: absolute;
    left: 302px;
    width: 599px;
    height: 358px;
    background: var(--card);
  }
  .card--front { top: 175px; }
  .card--back  { top: 678px; }

  .brand {
    position: absolute;
    display: flex;
    flex-direction: column;
    align-items: center;
    color: var(--navy);
    font-family: "Montserrat", sans-serif;
    font-weight: 500;
    text-align: center;
    text-transform: uppercase;
  }
  .brand__dot {
    border-radius: 50%;
    background: var(--aqua);
  }
  .card--front .brand {
    left: 0; right: 0; top: 88px;
  }
  .card--front .brand__dot { width: 84px; height: 84px; margin-bottom: 34px; }
  .card--front .brand__name { font-size: 32px; letter-spacing: 10px; line-height: 44px; }

  .card--back .brand {
    left: 50px; width: 190px; top: 70px;
  }
  .card--back .brand__dot { width: 46px; height: 46px; margin-bottom: 18px; }
  .card--back .brand__name { font-size: 18px; letter-spacing: 5px; line-height: 24px; }

  .name-band {
    position: absolute;
    left: 0;
    top: 202px;
    width: 282px;
    height: 63px;
    background: var(--aqua);
    color: var(--white);
    padding: 16px 0 0 49px;
  }
  .name-band__name {
    font-family: "Montserrat", sans-serif;
    font-weight: 700;
    font-size: 17px;
    line-height: 19px;
  }
  .name-band__role {
    font-family: "Roboto", sans-serif;
    font-weight: 400;
    font-size: 12.5px;
    line-height: 16px;
  }

  .contacts {
    position: absolute;
    left: 311px;
    top: 154px;
    list-style: none;
  }
  .contacts__item {
    display: flex;
    align-items: center;
    height: 31px;
    color: var(--navy);
    font-family: "Montserrat", sans-serif;
    font-weight: 500;
    font-size: 13.5px;
  }
  .contacts__icon {
    width: 20px;
    height: 20px;
    margin-right: 10px;
    flex: none;
  }
</style>
</head>
<body>
<main class="canvas">

  <section class="card card--front" aria-label="Card front">
    <div class="brand">
      <span class="brand__dot"></span>
      <span class="brand__name">Harborline<br>Lending</span>
    </div>
  </section>

  <section class="card card--back" aria-label="Card back">
    <div class="brand">
      <span class="brand__dot"></span>
      <span class="brand__name">Harborline<br>Lending</span>
    </div>

    <div class="name-band">
      <p class="name-band__name">NAME OF PERSON</p>
      <p class="name-band__role">Position</p>
    </div>

    <ul class="contacts">
      <li class="contacts__item">
        <svg class="contacts__icon" viewBox="0 0 20 20" aria-hidden="true">
          <path d="M5 3 L8 3 L9 7 L7 8.5 Q8.5 12 11.5 13 L13 11 L17 12 L17 15 Q16 17 13.5 16.5 Q6 14 3.5 6.5 Q3.5 4 5 3 Z" fill="var(--aqua)"/>
        </svg>
        000 000 0000
      </li>
      <li class="contacts__item">
        <svg class="contacts__icon" viewBox="0 0 20 20" aria-hidden="true">
          <rect x="5" y="1.5" width="10" height="17" rx="1.5" fill="none" stroke="var(--aqua)" stroke-width="1.4"/>
          <circle cx="10" cy="16" r="0.9" fill="var(--aqua)"/>
        </svg>
        000 000 0000
      </li>
      <li class="contacts__item">
        <svg class="contacts__icon" viewBox="0 0 20 20" aria-hidden="true">
          <circle cx="10" cy="10" r="8.5" fill="var(--aqua)"/>
          <g fill="none" stroke="var(--white)" stroke-width="1.1">
            <ellipse cx="10" cy="10" rx="3.5" ry="8.5"/>
            <line x1="1.5" y1="10" x2="18.5" y2="10"/>
            <line x1="10" y1="1.5" x2="10" y2="18.5"/>
            <path d="M3 5.5 H17 M3 14.5 H17"/>
          </g>
        </svg>
        www.website.com
      </li>
      <li class="contacts__item">
        <svg class="contacts__icon" viewBox="0 0 20 20" aria-hidden="true">
          <rect x="1" y="4" width="18" height="12" fill="var(--aqua)"/>
          <path d="M1 4 L10 11 L19 4 M1 16 L7.5 9.5 M19 16 L12.5 9.5" fill="none" stroke="var(--white)" stroke-width="1.1"/>
        </svg>
        info@website.com
      </li>
    </ul>
  </section>

</main>
</body>
</html>
```